Laundromat Grand Opening.

Laundromat /Grand opening. One side English, one side Spanish. Include the Address, Name, Raffle/Prizes and Grand opening date.
Ridgeview Suds Laundromat, 418 W. Harlan Ave. 2/7/2016. (555) 314-2297.

Industry/Entity Type

Coin

Colors
000000

Requirements
Nice to have
• Eye catching. Laundry theme.

```html
<!DOCTYPE html>
<html lang="en">
<head>
<meta charset="utf-8">
<title>Ridgeview Suds Laundromat – Grand Opening</title>
<link href="https://fonts.googleapis.com/css2?family=Josefin+Sans:wght@700&family=Source+Sans+3:ital,wght@0,400;0,600;0,700;1,400;1,700&display=swap" rel="stylesheet">
<style>
  :root {
    --navy: #23416f;
    --cream: #fbf9e6;
    --backdrop: #ebe6dc;
    --photo-blue: #6f8fd6;
    --photo-steel: #a9a39c;
    --ribbon-red: #d8342f;
    --blade-grey: #c4c6ca;
  }
  * { margin: 0; padding: 0; box-sizing: border-box; }
  html, body { width: 1200px; height: 900px; overflow: hidden; }
  body {
    background: var(--backdrop);
    font-family: "Source Sans 3", sans-serif;
    color: var(--navy);
    position: relative;
  }
  .invite {
    position: absolute;
    top: 58px;
    width: 535px;
    height: 792px;
    background: var(--cream);
    padding: 10px;
  }
  .invite--english { left: 35px; }
  .invite--spanish { left: 620px; }
  .invite__frame {
    width: 100%;
    height: 100%;
    border: 22px solid var(--navy);
    background: var(--cream);
    position: relative;
    text-align: center;
  }
  .hero-photo {
    position: absolute;
    left: 93px;
    top: 10px;
    width: 285px;
    height: 188px;
    background: linear-gradient(100deg, var(--photo-blue) 0%, var(--photo-steel) 45%, var(--photo-blue) 75%, #d8d4cc 100%);
    box-shadow: 4px 4px 8px rgba(0,0,0,0.25);
  }
  .brand__name {
    position: absolute;
    top: 232px;
    left: 0; right: 0;
    font-weight: 600;
    font-size: 30px;
    letter-spacing: 0.5px;
    line-height: 36px;
  }
  .brand__dot {
    position: absolute;
    top: 282px;
    left: 50%;
    width: 62px;
    height: 62px;
    margin-left: -31px;
    border-radius: 50%;
    background: var(--navy);
  }
  .invite__lead {
    position: absolute;
    top: 386px;
    left: 0; right: 0;
    font-size: 19px;
    line-height: 24px;
  }
  .invite__headline {
    position: absolute;
    top: 420px;
    left: 0; right: 0;
    font-family: "Josefin Sans", sans-serif;
    font-weight: 700;
    font-size: 34px;
    line-height: 40px;
    letter-spacing: 1.5px;
  }
  .ribbon-art {
    position: absolute;
    top: 460px;
    left: 178px;
    width: 115px;
    height: 100px;
    background: linear-gradient(120deg, var(--ribbon-red) 0%, var(--ribbon-red) 45%, var(--blade-grey) 55%, var(--blade-grey) 100%);
    opacity: 0.85;
  }
  .event-when {
    position: absolute;
    top: 568px;
    left: 0; right: 0;
    font-weight: 700;
    font-size: 19px;
    line-height: 25px;
  }
  .event-where {
    position: absolute;
    top: 626px;
    left: 0; right: 0;
    font-size: 15px;
    line-height: 21px;
  }
  .event-where__phone {
    font-weight: 700;
    display: inline-flex;
    align-items: center;
    gap: 4px;
  }
  .event-where__phone svg { width: 13px; height: 13px; }
  .event-prize {
    position: absolute;
    top: 696px;
    left: 0; right: 0;
    font-size: 15px;
    line-height: 20px;
    font-style: italic;
  }
  .invite--english .event-prize { font-weight: 700; }
  .invite--spanish .event-prize { font-weight: 400; }
  .invite--spanish .event-when { top: 572px; }
  .invite--spanish .event-where { top: 630px; }
</style>
</head>
<body>

<section class="invite invite--english" lang="en">
  <div class="invite__frame">
    <div class="hero-photo" role="img" aria-label="Photo collage of a row of front-loading washing machines in a laundromat"></div>
    <div class="brand__name">Ridgeview Suds Laundromat</div>
    <div class="brand__dot"></div>
    <p class="invite__lead">invites you to join us to celebrate</p>
    <h1 class="invite__headline">GRAND OPENING</h1>
    <div class="ribbon-art" role="img" aria-label="Illustration of scissors cutting a red ribbon"></div>
    <p class="event-when">Sunday | February 07, 2016<br>07:00 AM to 10:00 PM</p>
    <p class="event-where">418 W. Harlan Ave.,<br>Ridgeview, CA 95555, USA<br>
      <span class="event-where__phone"><svg viewBox="0 0 16 16" aria-hidden="true"><circle cx="8" cy="8" r="7" fill="none" stroke="currentColor" stroke-width="1.4"/><path d="M5.5 4.5c-.8.8-.6 3 1.2 4.8s4 2 4.8 1.2l-1.3-1.4-1.1.6C8.3 9.3 6.7 7.7 6.3 6.9l.6-1.1z" fill="currentColor"/></svg>(555) 314-2297</span></p>
    <p class="event-prize">Raffle prizes to be given away</p>
  </div>
</section>

<section class="invite invite--spanish" lang="es">
  <div class="invite__frame">
    <div class="hero-photo" role="img" aria-label="Collage de fotos de lavadoras en una lavandería"></div>
    <div class="brand__name">Ridgeview Suds Laundromat</div>
    <div class="brand__dot"></div>
    <p class="invite__lead">le invita a unirse a nosotros para celebrar</p>
    <h1 class="invite__headline">GRAN INAUGURACION</h1>
    <div class="ribbon-art" role="img" aria-label="Ilustración de tijeras cortando una cinta roja"></div>
    <p class="event-when">Domingo | 07 de febrero 2016<br>07:00 AM hasta las 10:00 PM</p>
    <p class="event-where">418 W. Harlan Ave.,<br>Ridgeview, CA 95555, USA<br>
      <span class="event-where__phone"><svg viewBox="0 0 16 16" aria-hidden="true"><circle cx="8" cy="8" r="7" fill="none" stroke="currentColor" stroke-width="1.4"/><path d="M5.5 4.5c-.8.8-.6 3 1.2 4.8s4 2 4.8 1.2l-1.3-1.4-1.1.6C8.3 9.3 6.7 7.7 6.3 6.9l.6-1.1z" fill="currentColor"/></svg>(555) 314-2297</span></p>
    <p class="event-prize">Premios de la rifa para ser regalado</p>
  </div>
</section>

</body>
</html>
```